Re-design of current business cards

We are updating our website with new colors and layout. Would like to re-design our business cards to co-ordinate. See attached pdf with new Brightwell website colors. We would also like to combine our 2 brands on the one business card. Attached is the new design for our Brightwell website, current business cards, which are one sided, brightwell logo in tiff, .ai for fonts. Brightwell logo font is Optimum, Lanterncove website home page image, Lanterncove brand statics for products which includes the logo for this brand.

Lanterncove brand will stay the dark gray on the website. See attached statics for product and website home page.
Updates

The business cards will be 2 sided. Brightwell Brand on one side and Lanterncove Brand on the other. The colors for Brightwell need to follow the color scheme of the brightwell website pdf I uploaded. The colors are a blue, lighter teal blue and white. Lanterncove needs to follow the dark gray color on files uploaded

Target Market(s)

The trade and consumers

Industry/Entity Type

Home Furnishing

Contact Information for Business Card

We are updating our website with new colors and layout. Would like to re-design our business cards to co-ordinate. We would also like to combine our 2 brands onto 1 2 sided business cards.

Requirements
Must have
• Colors that match our new website, see attached image.
• RGB colors
• navy -#152842
• teal - 98aeb9
• The gray color used for Lanterncove brands.
• ll logos and fonts should stay the same.

```html
<!DOCTYPE html>
<html lang="en">
<head>
<meta charset="utf-8">
<title>Brightwell / Lanterncove Business Card</title>
<link href="https://fonts.googleapis.com/css2?family=Belleza&family=Marcellus&family=Lato&display=swap" rel="stylesheet">
<style>
  :root {
    --page: #ececec;
    --navy: #152842;
    --navy-soft: #1d3152;
    --teal: #98aeb9;
    --white: #ffffff;
    --gray: #5c5c5c;
    --gray-soft: #636363;
    --type-light: #e9e9e9;
  }
  * { margin: 0; padding: 0; box-sizing: border-box; }
  html, body { width: 1200px; height: 1200px; overflow: hidden; background: var(--page); }
  .canvas { position: relative; width: 1200px; height: 1200px; }
  .card {
    position: absolute; left: 192px; width: 797px; height: 456px;
    border-radius: 22px; overflow: hidden;
    box-shadow: 0 6px 18px rgba(0,0,0,0.18);
  }
  .card--front { top: 56px; background: var(--navy); color: var(--white); font-family: "Belleza", sans-serif; }
  .card--back { top: 618px; background: var(--gray); color: var(--type-light); }
  .card__backdrop { position: absolute; inset: 0; }
  .card--front .card__backdrop { background: radial-gradient(ellipse at 50% 60%, var(--navy-soft), var(--navy) 70%); }
  .card--back .card__backdrop { background: radial-gradient(ellipse at 50% 55%, var(--gray-soft), var(--gray) 70%); }
  .edge-line { position: absolute; left: 0; top: 0; bottom: 0; width: 3px; background: var(--teal); }
  .icon-tab {
    position: absolute; left: 0; top: 274px; width: 26px; height: 136px;
    background: var(--teal); border-radius: 0 12px 12px 0;
    display: flex; flex-direction: column; justify-content: space-around; align-items: center; padding: 6px 0;
  }
  .icon-tab svg { width: 13px; height: 13px; fill: var(--white); }
  .person { position: absolute; left: 48px; top: 124px; }
  .person__name { font-size: 36px; font-weight: 400; letter-spacing: 1px; line-height: 1; }
  .person__title { font-size: 18px; margin-top: 10px; margin-left: 2px; }
  .brand { position: absolute; left: 390px; width: 390px; top: 26px; text-align: center; }
  .brand__mark { width: 80px; height: 80px; border-radius: 50%; background: var(--white); margin: 0 auto 14px; }
  .brand__name { font-size: 56px; letter-spacing: 2px; line-height: 1; }
  .brand__web { font-size: 19px; letter-spacing: 1px; margin-top: 8px; }
  .contacts { position: absolute; left: 48px; top: 284px; list-style: none; }
  .contacts li { font-size: 24px; letter-spacing: 0.5px; height: 39px; line-height: 39px; }
  .address { position: absolute; left: 390px; width: 390px; top: 318px; text-align: center; font-size: 19px; line-height: 25px; letter-spacing: 0.5px; }
  .sub-brand { position: absolute; right: 76px; top: 168px; text-align: right; }
  .sub-brand__name { font-family: "Marcellus", serif; font-size: 84px; line-height: 1; letter-spacing: 1px; text-transform: uppercase; }
  .sub-brand__by { font-family: "Lato", sans-serif; font-size: 20px; margin-top: 2px; letter-spacing: 0.5px; }
</style>
</head>
<body>
<main class="canvas">
  <section class="card card--front">
    <div class="card__backdrop" role="img" aria-label="Faint navy-toned photo of a furnished living room behind the card content"></div>
    <div class="edge-line"></div>
    <div class="icon-tab">
      <svg viewBox="0 0 24 24" aria-label="phone"><path d="M6.6 10.8a15 15 0 0 0 6.6 6.6l2.2-2.2c.3-.3.7-.4 1-.2 1.1.4 2.3.6 3.6.6.6 0 1 .4 1 1V20c0 .6-.4 1-1 1A17 17 0 0 1 3 4c0-.6.4-1 1-1h3.5c.6 0 1 .4 1 1 0 1.3.2 2.5.6 3.6.1.3 0 .7-.2 1z"/></svg>
      <svg viewBox="0 0 24 24" aria-label="fax"><path d="M6 3h12v5H6zM4 9h16a2 2 0 0 1 2 2v6h-4v4H6v-4H2v-6a2 2 0 0 1 2-2zm4 6v4h8v-4z"/></svg>
      <svg viewBox="0 0 24 24" aria-label="email"><path d="M2 5h20v14H2zm2 2v.5l8 5 8-5V7l-8 5z"/></svg>
    </div>
    <div class="person">
      <h1 class="person__name">DANA WHITFIELD</h1>
      <p class="person__title">Graphics/ Photography Director</p>
    </div>
    <div class="brand">
      <div class="brand__mark"></div>
      <p class="brand__name">BRIGHTWELL</p>
      <p class="brand__web">www.brightwell.com</p>
    </div>
    <ul class="contacts">
      <li>555.201.4870</li>
      <li>555.201.4871</li>
      <li>dwhitfield@brightwell.com</li>
    </ul>
    <p class="address">PO Box 214/1870 Cedar Ridge Rd<br>Millbrook, Vermont 05741</p>
  </section>

  <section class="card card--back">
    <div class="card__backdrop" role="img" aria-label="Faint gray-toned photo of a furnished room behind the brand name"></div>
    <div class="sub-brand">
      <p class="sub-brand__name">Lanterncove</p>
      <p class="sub-brand__by">by BRIGHTWELL</p>
    </div>
  </section>
</main>
</body>
</html>
```